Jewelry Shop Needs a Business Card Design

***We want a very sharp and unforgettable pantone for the Business Card. ***
***We do not want the business card or logo only in black, white and grey color!!!Please provide us a main color as our brand topic! Thanks!! ***

Mabel’s Nook is a Hong Kong based fine jewelry brand.

We want a very nice, simple and elegant business card design for Mabel's Nook Brand. The company's logo has been uploaded already.

You can design with below info:

Desmond Yip
Director
M: +852 94726305
T: +852 35842947
F: +852 35842949
E: desmond.yip@mabelsnook.example
9/F , Harbourlight Tower, 18-24 Fenwick Lane, Sai Wan Ho, Kowloon, Hong Kong

Target Market(s)

Mabel’s Nook philosophy is a jewelry icon of young, creative, trendy, fashionable, stylish, energetic, and elegant. For Mabel’s Nook, jewelry is one collection of artworks, the most important items in personal life.

Industry/Entity Type

Jewelry

Requirements
Must have
• We want a very sharp and unforgettable pantone for the Business Card.

```html
<!DOCTYPE html>
<html lang="en">
<head>
<meta charset="utf-8">
<title>Mabel’s Nook – Business Card</title>
<link rel="stylesheet" href="https://fonts.googleapis.com/css2?family=Cinzel:wght@400;500&family=Didact+Gothic&display=swap">
<style>
  :root {
    --backdrop: #141414;
    --card: #f5f4f2;
    --ink: #2b2b2b;
    --ink-soft: #5a5a5a;
    --brand: #b3124e;
    --brand-deep: #8e0c3c;
  }
  * { box-sizing: border-box; margin: 0; padding: 0; }
  html, body {
    width: 1200px;
    height: 675px;
    overflow: hidden;
    background: var(--backdrop);
  }
  .stage {
    width: 1200px;
    height: 675px;
    display: flex;
    align-items: center;
    justify-content: center;
    gap: 60px;
  }
  .card {
    width: 500px;
    height: 300px;
    background: var(--card);
    position: relative;
    display: flex;
    flex-direction: column;
    align-items: center;
  }
  /* Back side: brand */
  .card--brand { justify-content: center; gap: 18px; }
  .brand-dot {
    width: 76px;
    height: 76px;
    border-radius: 50%;
    background: var(--brand);
  }
  .brand-name {
    font-family: "Cinzel", serif;
    font-weight: 400;
    font-size: 18px;
    letter-spacing: 0.08em;
    color: var(--brand);
  }
  /* Front side: contact */
  .card--contact { padding-top: 78px; }
  .card--contact::after {
    content: "";
    position: absolute;
    left: 0;
    right: 0;
    bottom: 0;
    height: 6px;
    background: var(--brand);
  }
  .person-name {
    font-family: "Cinzel", serif;
    font-weight: 500;
    font-size: 24px;
    letter-spacing: 0.05em;
    color: var(--ink);
  }
  .person-title {
    font-family: "Didact Gothic", sans-serif;
    font-size: 14px;
    color: var(--brand-deep);
    margin-top: 2px;
  }
  .address {
    font-family: "Didact Gothic", sans-serif;
    font-size: 10px;
    line-height: 1.6;
    color: var(--ink-soft);
    text-align: center;
    margin-top: 34px;
  }
  .contact-grid {
    font-family: "Didact Gothic", sans-serif;
    font-size: 10px;
    color: var(--ink-soft);
    display: grid;
    grid-template-columns: auto auto auto auto;
    column-gap: 8px;
    row-gap: 4px;
    margin-top: 12px;
  }
  .contact-grid .label {
    font-weight: 700;
    color: var(--brand);
    text-align: right;
  }
  .contact-grid .value { margin-right: 10px; }
</style>
</head>
<body>
  <main class="stage">
    <section class="card card--brand" aria-label="Card back">
      <span class="brand-dot" aria-hidden="true"></span>
      <p class="brand-name">Mabel’s Nook</p>
    </section>

    <section class="card card--contact" aria-label="Card front">
      <h1 class="person-name">Desmond Yip</h1>
      <p class="person-title">Director</p>
      <p class="address">
        9/F , Harbourlight Tower, 18-24 Fenwick Lane<br>
        Sai Wan Ho, Kowloon Hong Kong
      </p>
      <div class="contact-grid">
        <span class="label">M</span><span class="value">+852 94726305</span>
        <span class="label">T</span><span class="value">+852 35842947</span>
        <span class="label">F</span><span class="value">+852 35842949</span>
        <span class="label">E</span><span class="value">desmond.yip@mabelsnook.example</span>
      </div>
    </section>
  </main>
</body>
</html>
```